letterhead design for a investing company*

Design an appealing business letterhead to match with our existing logo and attract new customers. Our customers are mainly corporate managers which are detail oriented and judge the company ability to perform a good service based on small details. A professional letterhead will give a good first impression.

Target Market(s)

New customers and business owners

Industry/Entity Type

Marketplace

Font styles to use
Sans Serif
Script

Requirements
Must have
• Must be a professional and elegant design that attracts interest from people who receives it

```html
<!DOCTYPE html>
<html lang="pt">
<head>
<meta charset="utf-8">
<title>BrightMend — Papel Timbrado</title>
<link rel="stylesheet" href="https://fonts.googleapis.com/css2?family=Poppins:wght@400;600&display=swap">
<style>
  :root {
    --navy: #121e3d;
    --gold: #fdbb14;
    --paper: #ffffff;
    --ink: #2b2f3a;
    --rule: #8a8d94;
  }
  html, body {
    margin: 0;
    padding: 0;
    overflow: hidden;
    background: var(--paper);
  }
  .letterhead {
    position: relative;
    width: 932px;
    height: 1200px;
    overflow: hidden;
    background: var(--paper);
    font-family: "Poppins", sans-serif;
    color: var(--ink);
  }
  .swoosh {
    position: absolute;
    left: 0;
    top: 0;
    width: 932px;
    height: 1200px;
  }
  .brand {
    position: absolute;
    left: 512px;
    top: 118px;
    display: flex;
    align-items: center;
    gap: 12px;
  }
  .brand-mark {
    width: 44px;
    height: 44px;
    border-radius: 50%;
    background: var(--gold);
    flex: none;
  }
  .brand-text {
    display: flex;
    flex-direction: column;
  }
  .brand-name {
    font-weight: 600;
    font-size: 44px;
    line-height: 1;
    color: var(--navy);
    letter-spacing: -0.5px;
  }
  .brand-tagline {
    font-weight: 400;
    font-size: 10.5px;
    letter-spacing: 1.4px;
    color: var(--navy);
    margin-top: 4px;
  }
  .footer {
    position: absolute;
    left: 96px;
    top: 1102px;
    width: 720px;
    font-size: 14px;
    line-height: 1.4;
  }
  .footer-address {
    margin: 0;
    padding-bottom: 2px;
    border-bottom: 1px solid var(--rule);
    white-space: nowrap;
  }
  .footer-contacts {
    margin: 5px 0 0;
    display: flex;
    align-items: center;
    gap: 4px;
    white-space: nowrap;
  }
  .footer-contacts svg {
    width: 11px;
    height: 11px;
    fill: var(--navy);
    flex: none;
  }
  .contact-item {
    display: inline-flex;
    align-items: center;
    gap: 3px;
    margin-right: 3px;
  }
</style>
</head>
<body>
<main class="letterhead">
  <svg class="swoosh" viewBox="0 0 932 1200" aria-hidden="true">
    <path d="M0,0 H932 C700,18 300,80 0,205 Z" fill="var(--navy)"/>
    <path d="M0,205 C300,80 700,18 932,0 C690,22 320,108 0,236 Z" fill="var(--gold)"/>
    <path d="M932,1060 C845,1144 715,1188 586,1200 H932 Z" fill="var(--gold)"/>
    <path d="M932,1068 C852,1148 724,1190 600,1200 H932 Z" fill="var(--navy)"/>
  </svg>

  <header class="brand">
    <span class="brand-mark"></span>
    <div class="brand-text">
      <span class="brand-name">BrightMend</span>
      <span class="brand-tagline">a qualidade em cada detalhe</span>
    </div>
  </header>

  <footer class="footer">
    <p class="footer-address">Rua das Acácias, condomínio Jardins do Sul, Edifício Lobito 114, Luanda- Angola , NIF 5000123456</p>
    <p class="footer-contacts">
      <span class="contact-item">
        <svg viewBox="0 0 24 24"><path d="M6.6 10.8a15.1 15.1 0 0 0 6.6 6.6l2.2-2.2a1 1 0 0 1 1-.25 11.4 11.4 0 0 0 3.6.57 1 1 0 0 1 1 1V20a1 1 0 0 1-1 1A17 17 0 0 1 3 4a1 1 0 0 1 1-1h3.5a1 1 0 0 1 1 1c0 1.25.2 2.45.57 3.57a1 1 0 0 1-.25 1Z"/></svg>
        923100457 / 9461208835
      </span>
      <span class="contact-item">
        <svg viewBox="0 0 24 24"><path d="M2 5h20v14H2Z M2 5l10 8 10-8" fill="var(--navy)"/><path d="M3 6l9 7 9-7" fill="none" stroke="#fff" stroke-width="2"/></svg>
        contactos@brightmend.com
      </span>
      <span class="contact-item">
        <svg viewBox="0 0 24 24"><circle cx="12" cy="12" r="10"/><path d="M7 6c2 1 3 3 2 5s-3 2-3 4M15 4c-1 2 0 3 2 4s3 4 1 7" fill="none" stroke="#fff" stroke-width="1.6"/></svg>
        www.brightmend.com
      </span>
    </p>
  </footer>
</main>
</body>
</html>
```